Hello Creative Minds!
Our business is after a elegant and classy flyer that draws attention!
The business is Velmora Turf - Lawn Rejuvenation Services. We provide services that maintain a healthy and vibrant green lawn through the tough Australian seasons. The products we use limits the water needed to keep grass green to a minimum - practically none at all! This not only helps the home owner or home seller but the environment by limiting the use of water that is needed to create a green lawn. The products we use are made from natural ingredients that are and pet friendly.
This fly will be our introductory offer to the market. Below are the required points that need to be on the flyer. Attached is the business logo, before & after pictures and 1 example of the LAYOUT not DESIGN of what the flyer should be laid out like or similar to. Feel free to use different 'Lawn Mower' pictures.
All the best; if you need any questions answered please feel free to message.
REQUIRED POINTS (Please re-phrase were possible);
*Instantly restores the natural green colour of grass – year round
*Lasts for up to 3 months
*Substantially reduces watering needs
*Pet friendly
*Stays green during droughts and water restrictions
*UV fade resistant
*Won’t bleed, run, or stain once absorbed into the grass
*Safe for the environment, pets and people
*Works in extreme heat, cold and frost
*Organic and natural – no harmful chemicals
*Reduces the amount of fertilizer
and water used on lawns
*Kerb appeal is essential for getting your property sold for the highest price possible
SERVICES & PRICING
Lawn maintenance (cut & trim) starting from $60
Lawn rejuvenation starting from $80 (Only $27 a month for 3 months)*
Package deal starting from $120
Introductory offer: 25% off all services. Refer a friend, when they book you receive another 25% off your next service.
LOCATIONS
Nowra to Sydney
CONTACT NUMBER
Will be posted with the winner - please leave an area for this.
SOCIAL MEDIA
Please add Chatterloop and Snapvista logo's
Updates
Competition has finished, thank you to all that have participated! I will review and comment on the flyers that need assistance. All the best with future designs!
Target Market(s)
home owners, home sellers, property developers, real estates and nursing homes and government housing.
Industry/Entity Type
Lawn Care
Look and feel
Each slider illustrates characteristics of the customer's brand and the style your logo design should communicate.

```html
<!DOCTYPE html>
<html lang="en">
<head>
<meta charset="utf-8">
<title>Velmora Turf – Lawn &amp; Landscaping Services</title>
<link rel="stylesheet" href="https://fonts.googleapis.com/css2?family=Montserrat:wght@600;700&family=Roboto:wght@400;700&display=swap">
<style>
  :root {
    --page: #ffffff;
    --grass-mid: #326d37;
    --grass-deep: #0b3a0f;
    --lime: #a9cf3b;
    --ink-green: #17461c;
    --white: #ffffff;
    --overlay: rgba(12, 40, 12, 0.72);
  }
  * { box-sizing: border-box; margin: 0; padding: 0; }
  html, body { width: 1200px; height: 1200px; overflow: hidden; background: var(--page); }
  body { position: relative; font-family: "Roboto", Arial, sans-serif; }

  .flyer {
    position: absolute; left: 189px; top: 68px; width: 828px; height: 1072px;
    background: var(--grass-deep); overflow: hidden; color: var(--white);
  }
  .hero-photo {
    position: absolute; left: 0; top: 0; width: 828px; height: 564px;
    background:
      radial-gradient(ellipse 60% 30% at 75% 8%, rgba(214, 170, 96, 0.55), transparent 70%),
      linear-gradient(180deg, #6b7a3e 0%, #4f7f2a 22%, #4c8f2c 40%, #3f832f 58%, var(--grass-mid) 78%, var(--grass-mid) 100%);
  }
  .hero-photo::after {
    content: ""; position: absolute; left: 0; right: 0; bottom: 0; height: 126px;
    background: var(--grass-deep);
  }
  .brand {
    position: absolute; left: 560px; top: 52px; width: 240px;
    font-family: "Montserrat", Arial, sans-serif; font-weight: 600; font-size: 28px;
    color: var(--white); text-align: center;
  }
  .headline {
    position: absolute; left: 61px; top: 258px;
    font-family: "Montserrat", Arial, sans-serif; font-weight: 700; font-size: 38.5px;
    letter-spacing: 0.2px; text-shadow: 0 2px 4px rgba(0,0,0,0.3);
  }
  .intro {
    position: absolute; left: 61px; top: 320px; width: 708px;
    font-size: 16px; line-height: 19.5px; text-align: justify;
  }

  .services {
    position: absolute; left: 34px; top: 441px; width: 759px; height: 223px;
    background: var(--white); padding: 4px; display: flex; gap: 4px;
  }
  .service { position: relative; flex: 1; overflow: hidden; }
  .service-photo { position: absolute; inset: 0; }
  .service--maintenance .service-photo {
    background: linear-gradient(160deg, #b9c9a4 0%, #6f9a4c 30%, #4e8a35 55%, #3f6e28 100%);
  }
  .service--rejuvenation .service-photo {
    background: linear-gradient(170deg, #1f4a1e 0%, #3a7b2b 35%, #5b9a36 65%, #4a8429 100%);
  }
  .service-label {
    position: absolute; left: 0; top: 0; height: 48px; width: 232px;
    background: var(--lime); clip-path: polygon(0 0, 100% 0, 93% 100%, 0 100%);
    font-family: "Montserrat", Arial, sans-serif; font-weight: 700; font-size: 19.5px;
    color: var(--ink-green); line-height: 48px; padding-left: 18px;
  }
  .price {
    position: absolute; right: 0; bottom: 0; width: 128px; height: 97px;
    background: var(--overlay); text-align: center; color: var(--lime);
    font-family: "Montserrat", Arial, sans-serif; font-weight: 700;
  }
  .price-note { display: block; font-size: 13.5px; margin-top: 12px; }
  .price-amount { display: block; font-size: 50px; line-height: 56px; }
  .price-amount sup { font-size: 24px; vertical-align: 20px; margin-right: 2px; }
  .price-amount .star { font-size: 18px; color: var(--white); vertical-align: 26px; }
  .footnote {
    position: absolute; left: 0; bottom: 0; padding: 4px 8px;
    background: linear-gradient(90deg, rgba(12,40,12,0.6), rgba(12,40,12,0));
    font-size: 11.5px; color: var(--white);
  }

  .offer-band {
    position: absolute; left: 34px; top: 674px; width: 759px; height: 97px;
    background: var(--lime); color: var(--ink-green); display: flex; align-items: center;
  }
  .package {
    width: 259px; padding-left: 26px;
    font-family: "Montserrat", Arial, sans-serif; font-weight: 700; font-size: 20.5px; line-height: 24px;
  }
  .offer-divider { width: 1px; height: 42px; background: var(--ink-green); }
  .intro-offer { padding-left: 39px; padding-right: 20px; font-size: 16px; line-height: 20px; }
  .intro-offer strong { font-weight: 700; }

  .benefits {
    position: absolute; top: 799px; left: 39px; width: 760px; display: flex;
    list-style: none;
  }
  .benefit-column { list-style: none; }
  .benefit-column:nth-child(1) { width: 256px; }
  .benefit-column:nth-child(2) { width: 258px; }
  .benefit-column:nth-child(3) { width: 230px; }
  .benefit-column li {
    position: relative; padding-left: 13px; font-size: 13.5px; line-height: 16.3px; margin-bottom: 8px;
  }
  .benefit-column li::before {
    content: ""; position: absolute; left: 0; top: 6px; width: 5px; height: 5px;
    border-radius: 50%; background: var(--lime);
  }

  .contact-bar {
    position: absolute; left: 0; bottom: 0; width: 828px; height: 105px; background: var(--grass-mid);
  }
  .contact-title {
    position: absolute; left: 39px; top: 20px;
    font-family: "Montserrat", Arial, sans-serif; font-weight: 700; font-size: 16.5px;
  }
  .contact-list {
    position: absolute; left: 39px; top: 50px; display: flex; gap: 18px; list-style: none;
    font-size: 16.5px; align-items: center;
  }
  .contact-list li { display: flex; align-items: center; gap: 7px; }
  .contact-list svg { width: 17px; height: 17px; fill: var(--white); }
  .contact-divider { position: absolute; left: 566px; top: 25px; width: 1px; height: 44px; background: rgba(255,255,255,0.6); }
  .social {
    position: absolute; left: 585px; top: 26px; display: flex; align-items: center; gap: 12px;
  }
  .social-title { font-family: "Montserrat", Arial, sans-serif; font-weight: 700; font-size: 16.5px; }
  .social-names { list-style: none; font-size: 12px; line-height: 17px; }
  .social-names li { display: flex; align-items: center; gap: 5px; }
  .social-names li::before { content: ""; width: 7px; height: 7px; border-radius: 50%; background: var(--lime); }
</style>
</head>
<body>
<main class="flyer">
  <div class="hero-photo" role="img" aria-label="Close-up photo of a lush green lawn with a lawn mower blurred in the background"></div>

  <div class="brand">Velmora Turf</div>

  <h1 class="headline">Lawn &amp; Landscaping Services</h1>
  <p class="intro">We provide services that maintain a healthy and vibrant green lawn through the tough Australian seasons. The products we use limits the water needed to keep grass green to a minimum - practically none at all! This not only helps the home owner or home seller but the environment by limiting the use of water that is needed to create a green lawn. The products we use are made from natural ingredients that are and pet friendly.</p>

  <section class="services">
    <article class="service service--maintenance">
      <div class="service-photo" role="img" aria-label="Photo of a lawn mower cutting grass in a garden"></div>
      <h2 class="service-label">Lawn Maintenance</h2>
      <div class="price">
        <span class="price-note">Starting from</span>
        <span class="price-amount"><sup>$</sup>60</span>
      </div>
    </article>
    <article class="service service--rejuvenation">
      <div class="service-photo" role="img" aria-label="Photo of a garden sprinkler watering a green lawn"></div>
      <h2 class="service-label">Lawn Rejuvenation</h2>
      <p class="footnote">* Only $27 a month for 3 months.</p>
      <div class="price">
        <span class="price-note">Starting from</span>
        <span class="price-amount"><sup>$</sup>80<span class="star">*</span></span>
      </div>
    </article>
  </section>

  <section class="offer-band">
    <p class="package">Package deal starting from $120</p>
    <span class="offer-divider"></span>
    <p class="intro-offer"><strong>Introductory Offer:</strong> 25% off all services. Refer a friend, when they book you receive another 25% off your next service.</p>
  </section>

  <div class="benefits">
    <ul class="benefit-column">
      <li>Instantly restores the natural green colour of grass for year round</li>
      <li>Lasts for up to 3 months</li>
      <li>Substantially reduces watering needs</li>
      <li>Pet friendly</li>
      <li>Stays green during droughts &amp; water restrictions</li>
    </ul>
    <ul class="benefit-column">
      <li>UV fade resistant</li>
      <li>Won’t bleed, run or stain once absorbed into the grass</li>
      <li>Safe for the environment,<br>pets &amp; people</li>
      <li>Works in extreme heat, cold &amp; frost</li>
    </ul>
    <ul class="benefit-column">
      <li>Organic and natural, no harmful chemicals</li>
      <li>Reduces the amount of fertilizer &amp; water used on lawns</li>
      <li>Kerb appeal is essential for getting your property sold for the highest price possible</li>
    </ul>
  </div>

  <footer class="contact-bar">
    <p class="contact-title">For more information, please contact us:</p>
    <ul class="contact-list">
      <li><svg viewBox="0 0 24 24" aria-hidden="true"><path d="M6.6 10.8a15.1 15.1 0 0 0 6.6 6.6l2.2-2.2c.3-.3.7-.4 1-.2 1.1.4 2.3.6 3.6.6.6 0 1 .4 1 1V20c0 .6-.4 1-1 1A17 17 0 0 1 3 4c0-.6.4-1 1-1h3.5c.6 0 1 .4 1 1 0 1.3.2 2.5.6 3.6.1.3 0 .7-.2 1z"/></svg>(000) 000-0000</li>
      <li><svg viewBox="0 0 24 24" aria-hidden="true" style="width:21px"><path d="M2 5h20v2l-10 6L2 7z M2 9l10 6 10-6v10H2z"/></svg>sales@email.com</li>
      <li><svg viewBox="0 0 24 24" aria-hidden="true"><path d="M10.6 13.4a1 1 0 0 1 0-1.4l3.5-3.5a1 1 0 1 1 1.4 1.4L12 13.4a1 1 0 0 1-1.4 0zM8 21a5 5 0 0 1-3.5-8.5l2.8-2.8 1.4 1.4-2.8 2.8a3 3 0 0 0 4.2 4.2l2.8-2.8 1.4 1.4-2.8 2.8A5 5 0 0 1 8 21zm8.7-6.3-1.4-1.4 2.8-2.8a3 3 0 0 0-4.2-4.2l-2.8 2.8-1.4-1.4 2.8-2.8a5 5 0 0 1 7 7z"/></svg>www.website.com</li>
    </ul>
    <span class="contact-divider"></span>
    <div class="social">
      <span class="social-title">Let’s connect</span>
      <ul class="social-names">
        <li>Chatterloop</li>
        <li>Snapvista</li>
      </ul>
    </div>
  </footer>
</main>
</body>
</html>
```